New Flyer Design Project - for sale units at The Lodge phase 3

on attached the A2 is full kitchen 1 bedroom, the A3 is gally kitchen and the B2 is the the 2 bedroom, on attached pictures the room with 2 queen beds is only for the 2 bedroom

This is going to be used to sale the units (real estate sale) so the layout could possibly be text and then pictures maybe 1 bedroom on one side and 2 on the back?

Experience the Modern Luxury of the New Phase 3 Building of the
Lodge at Harlow Bend

* Opening Spring 2019

* America's #17 Family Resort; Tennessee's Only Ranked Resort

1 Bedroom Bunk Suite (Galley Kitchen) - $199,000; Sleeps 6

* Private King Master Bedroom

* Bunk Bed Galley

* Granite Counters Throughout

* Fully Furnished with Custom Furnishings

* Private Balcony

* Equipped Galley Kitchen

* In Unit Laundry

* Queen Sleeper Sofa

1 Bedroom Bunk Suite (Full Kitchen) - $209,000; Sleeps 6

* Bunk Bed Galley

* Granite Counters throughout

* Equipped Full Kitchen

* Completely Furnished with Custom Furnishings

* Private Balcony

* In Unit Laundry

* Queen Sleeper Sofa

2 Bedroom Bunk Suite (Full Kitchen) - $249,000; Sleeps 10

* Private King Master Bedroom with On-Suite Bathroom

* Two Queen Bedroom

* Bunk Bed Galley

* Full Kitchen

* Private Balcony

* In Unit Laundry

* Queen Sleeper Sofa

Target Market(s)

people wanting to buy units in phase 3 of The Lodge at Harlow Bend

Industry/Entity Type

Real Estate Development

Requirements
Must have
• attached text to describe units and price
• pictures and layouts
• Contact Dale Porter
• 865-730-2958 Dale@brightfernretreats.example
Nice to have
• brand and logo
Should not have
• it should not be plain this is m ore of a luxury project

```html
<!DOCTYPE html>
<html lang="en">
<head>
<meta charset="utf-8">
<title>The Lodge at Harlow Bend – Phase 3 Suites for Sale</title>
<link rel="stylesheet" href="https://fonts.googleapis.com/css2?family=Roboto+Condensed:wght@400;700&display=swap">
<style>
  :root{
    --backdrop:#a09e9f;
    --paper:#ffffff;
    --tan:#d39d62;
    --slate:#5c8a99;
    --brown:#6d5342;
    --ink:#46321f;
    --rule:#fbeedb;
    --cream:#f6e7cf;
  }
  *{box-sizing:border-box;margin:0;padding:0}
  html,body{width:1200px;height:800px;overflow:hidden;background:var(--backdrop)}
  body{font-family:"Roboto Condensed",Arial,sans-serif;position:relative}

  .flyer{position:absolute;left:322px;top:40px;width:556px;height:720px;background:var(--paper);overflow:hidden;box-shadow:0 6px 18px rgba(0,0,0,.25)}

  .hero-photo{position:absolute;left:0;top:0;width:556px;height:230px;
    background:linear-gradient(100deg,#7f8d5c 0%,#c9cfb5 18%,#eef0e6 34%,#a7b08a 55%,#3b2f2a 68%,#e9ecdf 78%,#b8be9c 100%)}
  .hero-band{position:absolute;left:0;top:230px;width:556px;height:16px;background:var(--slate)}

  .brand{position:absolute;left:50%;top:200px;transform:translateX(-50%);display:flex;align-items:center;gap:8px;
    background:var(--paper);padding:7px 14px;border-radius:2px;box-shadow:0 1px 4px rgba(0,0,0,.2)}
  .brand-square{width:20px;height:20px;background:var(--tan)}
  .brand-name{font-size:18px;font-weight:700;color:var(--brown);letter-spacing:.5px;white-space:nowrap}

  .gallery{position:absolute;left:18px;top:260px;width:520px;display:flex;justify-content:space-between}
  .gallery-photo{width:166px;height:92px;border:3px solid var(--paper);box-shadow:0 0 0 1px #ddd}
  .photo-kitchen{background:linear-gradient(120deg,#c3c6a4,#8f8a72 45%,#e4e1d8 70%,#4a3c33)}
  .photo-bath{background:linear-gradient(120deg,#eef0e8,#c6cfa4 40%,#ffffff 60%,#3d322c)}
  .photo-dining{background:linear-gradient(120deg,#dfe3cf,#a8b686 45%,#3c3029 70%,#bfc8a8)}

  .listings{position:absolute;left:0;top:366px;width:556px;height:280px;background:var(--tan);
    display:flex;justify-content:space-between;padding:0 18px}
  .suite{width:168px;position:relative}
  .suite-tab{position:relative;top:-11px;display:inline-block;background:var(--slate);color:#fff;font-weight:700;
    font-size:11.5px;padding:4px 10px;border-radius:2px 11px 2px 2px;letter-spacing:.3px;white-space:nowrap}
  .suite-kitchen{font-size:10px;color:var(--ink);text-transform:uppercase;margin-top:-6px;line-height:12px}
  .suite-price{font-size:12px;font-weight:700;color:var(--ink);margin-bottom:7px;line-height:14px}
  .features{list-style:none}
  .features li{font-size:10px;line-height:11.5px;color:var(--ink);text-transform:uppercase;
    border-left:1.5px solid var(--rule);padding-left:7px;margin:0 0 6px 5px}

  .divider{position:absolute;left:0;top:646px;width:556px;height:7px;background:var(--paper)}
  .contact-bar{position:absolute;left:0;top:653px;width:556px;height:67px;background:var(--brown);
    display:flex;align-items:center;justify-content:center;gap:16px;color:var(--cream);font-size:13px}
  .contact-item{display:flex;align-items:center;gap:6px}
  .contact-item svg{width:14px;height:14px}
</style>
</head>
<body>
  <main class="flyer">
    <div class="hero-photo" role="img" aria-label="Photo of a suite bedroom with two queen beds, green walls and a large window"></div>
    <div class="hero-band"></div>
    <div class="brand">
      <span class="brand-square"></span>
      <span class="brand-name">The Lodge at Harlow Bend</span>
    </div>

    <section class="gallery">
      <div class="gallery-photo photo-kitchen" role="img" aria-label="Photo of the galley kitchen and dining table"></div>
      <div class="gallery-photo photo-bath" role="img" aria-label="Photo of the bathroom vanity with granite counter"></div>
      <div class="gallery-photo photo-dining" role="img" aria-label="Photo of the full kitchen and dining area"></div>
    </section>

    <section class="listings">
      <article class="suite">
        <h2 class="suite-tab">1 BEDROOM BUNK SUITE</h2>
        <p class="suite-kitchen">(Galley Kitchen)</p>
        <p class="suite-price">$199,000; SLEEPS 6</p>
        <ul class="features">
          <li>Private King<br>Master Bedroom</li>
          <li>Bunk Bed Galley</li>
          <li>Granite Counters<br>Throughout</li>
          <li>Fully Furnished<br>with Custom Furnishings</li>
          <li>Private Balcony</li>
          <li>Equipped Galley Kitchen</li>
          <li>In Unit Laundry</li>
          <li>Queen Sleeper Sofa</li>
        </ul>
      </article>
      <article class="suite">
        <h2 class="suite-tab">1 BEDROOM BUNK SUITE</h2>
        <p class="suite-kitchen">(Fully Kitchen)</p>
        <p class="suite-price">$ 209,000; SLEEPS 6</p>
        <ul class="features">
          <li>Private King<br>Master Bedroom</li>
          <li>Bunk Bed Galley</li>
          <li>Granite Counters<br>Throughout</li>
          <li>Equipped Full<br>Kitchen</li>
          <li>Completely Furnished<br>with Custom Furnishing</li>
          <li>Private Balcony</li>
          <li>In Unit Laundry</li>
          <li>Queen Sleeper Sofa</li>
        </ul>
      </article>
      <article class="suite">
        <h2 class="suite-tab">2 BEDROOM BUNK SUITE</h2>
        <p class="suite-kitchen">(Full Kitchen)</p>
        <p class="suite-price">$ 249,000; SLEEPS 10</p>
        <ul class="features">
          <li>Private King Master<br>Bedroom with On-Suite<br>Bathroom</li>
          <li>Two Queen Bedroom</li>
          <li>Bunk Bed Galley</li>
          <li>Granite Counters<br>Throughout</li>
          <li>Full Kitchen</li>
          <li>Completely Furnished<br>with Custom Furnishings</li>
          <li>Private Balcony</li>
          <li>In Unit Laundry</li>
          <li>Queen Sleeper Sofa</li>
        </ul>
      </article>
    </section>

    <div class="divider"></div>
    <footer class="contact-bar">
      <span class="contact-item">
        <svg viewBox="0 0 16 16" aria-hidden="true"><circle cx="8" cy="8" r="8" fill="#f6e7cf"/><path d="M5.2 4.2l1.4-.3.8 2-1 .7a5 5 0 0 0 2.9 2.9l.7-1 2 .8-.3 1.4c-3.6.3-6.8-2.9-6.5-6.5z" fill="#6d5342"/></svg>
        865-730-2958
      </span>
      <span class="contact-item">
        <svg viewBox="0 0 16 16" aria-hidden="true"><circle cx="8" cy="8" r="8" fill="#f6e7cf"/><rect x="4" y="5.2" width="8" height="5.6" fill="none" stroke="#6d5342" stroke-width="1"/><path d="M4 5.4l4 3 4-3" fill="none" stroke="#6d5342" stroke-width="1"/></svg>
        Dale@brightfernretreats.example
      </span>
    </footer>
  </main>
</body>
</html>
```